Dravetti Business Cards

We need a business card design for Dravetti Mining.

This is a B2B company that buys and sells large machinery tires within the coal mining industry. The design should the strong, crisp and masculine. I have uploaded the company logo and rough mock-up of what the back of the card should look like. the front of the card should have the same look/feel as the back. I need editable templates for both the front and the back of the card.

Color scheme should be grey/green/black

Contact information to include on the card:
Name: Owen Pellsworth
Title: Managing Director
Phone: 972-555-0143
Address: 3157 Brantley #5 Dallas, TX 75209
Email: Owen@Dravetti-example.com

I am also opening a contest for letterhead design. If you submit a business card design, please also submit a letterhead design with the same look/feel. The winner of the business card design will also will the letter head and be paid for both.

Target Market(s)

Procurement men/women in the coal mining industry

Industry/Entity Type

Coal Mining

```html
<!DOCTYPE html>
<html lang="en">
<head>
<meta charset="utf-8">
<title>Dravetti Mining Letterhead</title>
<link href="https://fonts.googleapis.com/css2?family=Questrial&family=Tinos:wght@400;700&display=swap" rel="stylesheet">
<style>
  :root {
    --backdrop: #3f5d61;
    --paper: #ffffff;
    --ink: #0b0c0c;
    --band: #0a0b0b;
    --accent: #5ee038;
    --light: #f2f2f2;
  }
  * { box-sizing: border-box; margin: 0; padding: 0; }
  html, body {
    width: 1200px;
    height: 900px;
    overflow: hidden;
    background: var(--backdrop);
  }
  .letterhead {
    position: absolute;
    left: 280px;
    top: 36px;
    width: 640px;
    height: 828px;
    background: var(--paper);
    box-shadow: 0 10px 30px rgba(0,0,0,0.35);
    overflow: hidden;
  }
  .header-band, .footer-band {
    position: absolute;
    left: 0;
    width: 640px;
    display: block;
  }
  .header-band { top: 0; height: 130px; }
  .footer-band { bottom: 0; height: 150px; }
  .brand-name {
    position: absolute;
    left: 26px;
    top: 30px;
    font-family: "Questrial", sans-serif;
    font-size: 34px;
    line-height: 1;
    letter-spacing: 1px;
    color: var(--light);
    white-space: nowrap;
  }
  .letter-date {
    position: absolute;
    right: 55px;
    top: 140px;
    font-family: "Tinos", serif;
    font-size: 11px;
    color: var(--ink);
  }
  .letter-date sup { font-size: 7px; }
  .letter-body {
    position: absolute;
    left: 70px;
    top: 196px;
    width: 500px;
    font-family: "Tinos", serif;
    font-size: 10px;
    line-height: 1.3;
    text-align: center;
    color: var(--ink);
  }
  .letter-body p { margin-bottom: 38px; }
  .signatory {
    position: absolute;
    right: 18px;
    bottom: 12px;
    text-align: right;
    font-family: "Questrial", sans-serif;
    color: var(--light);
  }
  .signatory .name {
    font-size: 20px;
    letter-spacing: 0.5px;
    line-height: 1;
  }
  .signatory .name .initial { color: var(--accent); }
  .signatory .role {
    display: inline-block;
    background: var(--light);
    color: var(--ink);
    font-size: 10.5px;
    letter-spacing: 0.6px;
    padding: 1px 8px;
    margin: 2px 0 6px;
    border-bottom: 2px solid var(--accent);
  }
  .signatory .line {
    font-size: 11.5px;
    line-height: 1.45;
    letter-spacing: 0.3px;
  }
</style>
</head>
<body>
  <article class="letterhead">
    <svg class="header-band" viewBox="0 0 640 130" aria-hidden="true">
      <path d="M0,0 H640 V48 C520,56 420,70 300,84 C190,96 80,106 0,112 Z" fill="#0a0b0b"/>
    </svg>
    <div class="brand-name">DRAVETTI MINING</div>

    <div class="letter-date">October, 4<sup>th</sup> 2013</div>

    <div class="letter-body">
      <p>Lorem ipsum dolor sit amet, consectetuer adipiscing elit, sed diam nonummy nibh euismod tincidunt ut laoreet dolore magna aliquam erat volutpat. Ut wisi enim ad minim veniam, quis nostrud exerci tation ullamcorper suscipit lobortis nisl ut aliquip ex ea commodo consequat.</p>
      <p>Duis autem vel eum iriure dolor in hendrerit in vulputate velit esse molestie consequat, vel illum dolore eu feugiat nulla facilisis at vero eros et accumsan et iusto odio dignissim qui blandit praesent luptatum zzril delenit augue duis dolore te feugait nulla facilisi. Nam liber tempor cum soluta nobis eleifend option congue nihil imperdiet doming id quod mazim placerat facer possim assum.</p>
      <p>Typi non habent claritatem insitam; est usus legentis in iis qui facit eorum claritatem. Investigationes demonstraverunt lectores legere me lius quod ii legunt saepius. Claritas est etiam processus dynamicus, qui sequitur mutationem consuetudium lectorum. Mirum est notare quam littera gothica, quam nunc putamus parum claram, anteposuerit litterarum formas humanitatis per seacula quarta decima et quinta decima. Eodem modo typi, qui nunc nobis videntur parum clari, fiant sollemnes in futurum.</p>
    </div>

    <svg class="footer-band" viewBox="0 0 640 150" aria-hidden="true">
      <path d="M0,150 V68 C140,52 330,40 470,26 C550,18 610,10 640,6 V150 Z" fill="#0a0b0b"/>
    </svg>
    <div class="signatory">
      <div class="name"><span class="initial">O</span>WEN <span class="initial">P</span>ELLSWORTH</div>
      <div class="role">MANAGING DIRECTOR</div>
      <div class="line">OWEN@DRAVETTI-EXAMPLE.COM</div>
      <div class="line">972.555.0143</div>
      <div class="line">3157 BRANTLEY #5 DALLAS, TX 75209</div>
    </div>
  </article>
</body>
</html>
```